Promotional poster for a vintage motorcycle show.

Vertically oriented, based on 11 x 17 inch proportions

Though not to the exclusion of other design concepts, stylistically perhaps something evoking a vintage (early-mid 20th century) 2-3 color silk screen style event poster.

In addition to some sort of eyecatching, vintage / antique motorbike oriented graphic (preferably not Corwin Baxley based), the poster should include the following text and info:

3rd Annual Milo Quenby Vintage Motorcycle Show
Bordentown City, N.J.
October 1st (rain date Oct. 2nd)
11am-4pm

Presented in conjunction with the 27th Annual Thistlewood Fair

For further info, or to register your pre-1992 bike contact:
Marty@wheelvaultex.com or 555-204-8913

Sponsored by:
UptownHallowmereGuildway.com
Wheelvaultex.com

Must have
• See above project description
Nice to have
• See above project describtion

```html
<!DOCTYPE html>
<html lang="en">
<head>
<meta charset="utf-8">
<title>3rd Annual Milo Quenby Vintage Motorcycle Show</title>
<link rel="stylesheet" href="https://fonts.googleapis.com/css2?family=Londrina+Solid:wght@400;900&family=Bungee+Inline&family=Cabin+Condensed:wght@500;600;700&display=swap">
<style>
  :root {
    --ink: #7b643a;
    --ink-light: #9a8257;
    --ink-dark: #5e4c2b;
    --paper: #ffffff;
  }
  html, body { margin: 0; padding: 0; overflow: hidden; background: var(--paper); }
  .poster { display: block; width: 777px; height: 1200px; }
  .headline { font-family: "Londrina Solid", sans-serif; font-weight: 400; fill: var(--paper); }
  .headline-ink { font-family: "Londrina Solid", sans-serif; font-weight: 400; fill: var(--ink); }
  .name { font-family: "Bungee Inline", sans-serif; fill: var(--paper); }
  .label { font-family: "Cabin Condensed", sans-serif; font-weight: 600; }
  .on-ink { fill: var(--paper); }
  .on-paper { fill: var(--ink); }
  .rule { stroke: var(--ink); stroke-width: 2; fill: none; }
  .rule-light { stroke: var(--paper); stroke-width: 1.5; fill: none; }
</style>
</head>
<body>
<svg class="poster" viewBox="0 0 777 1200" xmlns="http://www.w3.org/2000/svg">
  <defs>
    <linearGradient id="bikeTone" x1="0" y1="0" x2="1" y2="1">
      <stop offset="0" stop-color="#8d7548"/>
      <stop offset="0.5" stop-color="#b8a57f"/>
      <stop offset="1" stop-color="#7b643a"/>
    </linearGradient>
    <path id="ribbonArc" d="M186,985 Q324,907 466,985"/>
  </defs>

  <!-- ground colours -->
  <rect class="background" width="777" height="1200" fill="var(--ink)"/>
  <path class="paper-field" fill="var(--paper)"
        d="M0,480 L60,478 L120,482 L200,478 L282,484 L272,520 L290,548 L262,562 L400,550 L520,548 L580,600 L580,664 L700,676 L777,704 L777,1200 L0,1200 L0,656 L60,640 L130,612 L118,582 L40,572 L0,566 Z"/>

  <!-- top banner -->
  <rect class="festival-pill" x="70" y="70" width="638" height="27" rx="13.5" fill="var(--paper)"/>
  <text class="label on-paper" x="389" y="89.5" font-size="16.5" text-anchor="middle" font-weight="700">PRESENTED IN CONJUNCTION WITH THE 27<tspan font-size="10" dy="-6">TH</tspan><tspan dy="6"> ANNUAL THISTLEWOOD FAIR</tspan></text>

  <!-- headline -->
  <text class="headline" x="80" y="264" font-size="190" textLength="116" lengthAdjust="spacingAndGlyphs">3</text>
  <text class="headline" x="204" y="220" font-size="120" textLength="140" lengthAdjust="spacingAndGlyphs">RD</text>
  <text class="headline" x="196" y="264" font-size="44" textLength="144" lengthAdjust="spacingAndGlyphs">ANNUAL</text>
  <text class="headline" x="80" y="352" font-size="96" textLength="264" lengthAdjust="spacingAndGlyphs">VINTAGE</text>

  <text class="name" x="540" y="232" font-size="132" text-anchor="middle" textLength="328" lengthAdjust="spacingAndGlyphs">MILO</text>
  <text class="name" x="540" y="348" font-size="128" text-anchor="middle" textLength="328" lengthAdjust="spacingAndGlyphs">QUENBY</text>

  <text class="headline" x="72" y="472" font-size="118" textLength="636" lengthAdjust="spacingAndGlyphs">MOTORCYCLE</text>
  <text class="headline-ink" x="72" y="552" font-size="70" textLength="188" lengthAdjust="spacingAndGlyphs">SHOW</text>

  <!-- motorcycle illustration area -->
  <path class="bike-art" fill="url(#bikeTone)" role="img" aria-label="Screen-printed illustration of a vintage motorcycle seen from the side"
        d="M270,566 L300,548 L440,526 L540,524 L584,560 L584,672 L700,684 L700,936 L472,936 L462,912 L190,906 L64,880 L56,720 L92,640 L180,604 Z"/>

  <!-- sponsor tag -->
  <g class="sponsors">
    <path class="rule-light" d="M592,508 L592,494 L704,494 L704,508"/>
    <line class="rule-light" x1="648" y1="484" x2="648" y2="494"/>
    <text class="label on-ink" x="648" y="512" font-size="12.5" text-anchor="middle" font-weight="700">SPONSORED BY:</text>
    <line class="rule-light" x1="594" y1="518" x2="702" y2="518"/>
    <text class="label on-ink" font-size="12.5" text-anchor="middle">
      <tspan x="648" y="535">UPTOWN</tspan>
      <tspan x="648" y="549">HALLOWMERE</tspan>
      <tspan x="648" y="563">GUILDWAY</tspan>
      <tspan x="648" y="577">.COM</tspan>
    </text>
    <path class="rule-light" d="M594,584 L594,620 L648,634 L702,620 L702,584"/>
    <text class="label on-ink" font-size="12.5" text-anchor="middle">
      <tspan x="648" y="601">WHEELVAULTEX</tspan>
      <tspan x="648" y="615">.COM</tspan>
    </text>
    <g class="rule-light">
      <line x1="582" y1="622" x2="596" y2="630"/><line x1="590" y1="640" x2="604" y2="642"/>
      <line x1="714" y1="622" x2="700" y2="630"/><line x1="706" y1="640" x2="692" y2="642"/>
      <line x1="648" y1="644" x2="648" y2="660"/>
    </g>
  </g>

  <!-- location ribbon -->
  <g class="location">
    <path fill="var(--ink)" d="M192,968 L140,990 L162,1000 L146,1014 L198,1004 Z"/>
    <path fill="var(--ink)" d="M456,968 L508,990 L486,1000 L502,1014 L450,1004 Z"/>
    <path fill="var(--ink)" d="M186,958 Q324,878 466,958 L466,996 Q324,916 186,996 Z"/>
    <text class="label on-ink" font-size="24" font-weight="600" text-anchor="middle" letter-spacing="1">
      <textPath href="#ribbonArc" startOffset="50%">BORDENTOWN CITY, N.J.</textPath>
    </text>
  </g>

  <!-- date & time -->
  <g class="schedule">
    <path class="rule" d="M216,988 L216,1048 L356,1048 L356,976"/>
    <line class="rule" x1="364" y1="958" x2="364" y2="1070"/>
    <path class="rule" d="M372,970 L372,1048 L428,1048 L428,985"/>
    <line class="rule" x1="216" y1="1020" x2="356" y2="1020"/>
    <line class="rule" x1="372" y1="1016" x2="428" y2="1016"/>
    <text class="label on-paper" x="224" y="1012" font-size="25" textLength="128" lengthAdjust="spacingAndGlyphs">OCTOBER 1<tspan font-size="12" dy="-10">ST</tspan></text>
    <text class="label on-paper" x="286" y="1040" font-size="13" text-anchor="middle">[RAIN DATE OCT. 2<tspan font-size="8" dy="-5">ND</tspan><tspan dy="5">]</tspan></text>
    <text class="label on-paper" x="378" y="1008" font-size="25">11<tspan font-size="13" dy="-9">AM</tspan></text>
    <text class="label on-paper" x="382" y="1041" font-size="25">4<tspan font-size="13" dy="-9">PM</tspan></text>
    <g class="rule" stroke-width="1.5">
      <line x1="200" y1="1052" x2="180" y2="1060"/><line x1="214" y1="1060" x2="200" y2="1076"/>
      <line x1="236" y1="1058" x2="228" y2="1080"/><line x1="266" y1="1058" x2="262" y2="1082"/>
      <line x1="298" y1="1058" x2="300" y2="1084"/><line x1="330" y1="1058" x2="338" y2="1080"/>
      <line x1="400" y1="1058" x2="408" y2="1078"/><line x1="430" y1="1058" x2="444" y2="1074"/>
      <line x1="444" y1="1050" x2="464" y2="1058"/>
    </g>
  </g>

  <!-- footer -->
  <g class="contact">
    <text class="label on-paper" x="70" y="1131" font-size="10.5">FOR FURTHER INFO, OR TO REGISTER YOUR</text>
    <rect class="rule" x="278" y="1116" width="74" height="20" stroke-width="1.5"/>
    <line class="rule" x1="315" y1="1108" x2="315" y2="1116" stroke-width="1.5"/>
    <line class="rule" x1="315" y1="1136" x2="315" y2="1144" stroke-width="1.5"/>
    <text class="label on-paper" x="315" y="1131" font-size="12.5" text-anchor="middle">PRE–1992</text>
    <text class="label on-paper" x="361" y="1131" font-size="10.5">BIKE CONTACT: <tspan font-size="14.5" font-weight="500">Marty@wheelvaultex.com</tspan> OR <tspan font-size="14.5" font-weight="500">555 204 8913</tspan></text>
  </g>
</svg>
</body>
</html>
```